Lanternfield Advisory logo/business card design -- a digital consulting company

I've just restarted a consulting company I had years ago--Lanternfield Advisory. Now I need a new business card and updated logo. The original logo was simple enough: a chart-like progression atop a grid (see the attached file). I do strategy work, and the chart is meant to show incremental growth and profit. I'd like the reincarnation of my logo to be 3D, with both the grid and arrow rotated on their axis.

I'll want to use the logo on my website as well. I'm open to color schemes, fonts, etc.

Target Market(s)

Business-to-Business. Target market is corporate.

Industry/Entity Type

Business

Contact Information for Business Card

Logo on one-side; name and other contact info on the back

Font styles to use
Serif
Sans Serif

Requirements
Nice to have
• Lanternfield Advisory refers to the concept of "bootstrapping" or making incremental changes to grow with minimal risk and financial exposure, and self-sufficiency (think of the phrase "to pull oneself by one's bootstraps.")

```html
<!DOCTYPE html>
<html lang="en">
<head>
<meta charset="utf-8">
<title>Lanternfield Advisory – Business Card</title>
<link href="https://fonts.googleapis.com/css2?family=Questrial&display=swap" rel="stylesheet">
<style>
  :root {
    --bg: #2a2b2d;
    --card-light: #3a4149;
    --card-dark: #20252b;
    --accent: #e8262f;
    --text: #e9ecef;
    --muted: #c9ced3;
    --divider: rgba(255,255,255,0.28);
  }
  * { margin: 0; padding: 0; box-sizing: border-box; }
  html, body { width: 1200px; height: 900px; overflow: hidden; }
  body {
    background: var(--bg);
    font-family: "Questrial", "Century Gothic", sans-serif;
    display: flex;
    flex-direction: column;
    align-items: center;
    justify-content: center;
    gap: 60px;
  }
  .card {
    width: 640px;
    height: 366px;
    background: radial-gradient(ellipse at 60% 35%, var(--card-light), var(--card-dark) 80%);
    box-shadow: 0 14px 30px rgba(0,0,0,0.55);
    position: relative;
    color: var(--text);
  }
  /* Back side: name and contact */
  .card-back .identity {
    position: absolute;
    left: 70px;
    top: 150px;
    text-align: right;
    width: 210px;
  }
  .identity .person-name {
    color: var(--accent);
    font-size: 28px;
    font-weight: 700;
    letter-spacing: 0.3px;
    white-space: nowrap;
  }
  .identity .person-role {
    font-size: 15px;
    color: var(--muted);
    margin-top: 2px;
  }
  .card-back .divider {
    position: absolute;
    left: 312px;
    top: 95px;
    width: 1px;
    height: 175px;
    background: linear-gradient(to bottom, transparent, var(--divider), transparent);
  }
  .card-back .contact {
    position: absolute;
    left: 340px;
    top: 112px;
    font-size: 14px;
    line-height: 1.35;
    color: var(--text);
  }
  .contact .address { margin-bottom: 14px; }
  .contact .line { display: flex; align-items: center; gap: 8px; }
  .contact .line svg { width: 11px; height: 11px; flex: none; }
  /* Front side: brand name */
  .card-front .brand {
    position: absolute;
    inset: 0;
    display: flex;
    align-items: center;
    justify-content: center;
    gap: 14px;
  }
  .brand .brand-mark {
    width: 22px; height: 22px;
    border-radius: 50%;
    background: var(--accent);
  }
  .brand .brand-name {
    color: var(--accent);
    font-size: 34px;
    letter-spacing: 2px;
    text-transform: uppercase;
  }
</style>
</head>
<body>
  <section class="card card-back" aria-label="Business card back">
    <div class="identity">
      <div class="person-name">Martin Hale</div>
      <div class="person-role">Director</div>
    </div>
    <div class="divider"></div>
    <div class="contact">
      <div class="address">12 Harrow Lane<br>Easton Park, Sample, 0000</div>
      <div class="line">
        <svg viewBox="0 0 12 12"><path d="M2 1h3l1 3-1.5 1a6 6 0 0 0 2.5 2.5L8 6l3 1v3c0 .6-.4 1-1 1A9 9 0 0 1 1 2c0-.6.4-1 1-1z" fill="var(--accent)"/></svg>
        <span>0987 654 321</span>
      </div>
      <div class="line">
        <svg viewBox="0 0 12 12"><rect x="1" y="2.5" width="10" height="7" fill="var(--accent)"/><path d="M1 2.5l5 4 5-4" stroke="#20252b" fill="none"/></svg>
        <span>martin@lanternfieldadvisory.com</span>
      </div>
      <div class="line">
        <svg viewBox="0 0 12 12"><circle cx="6" cy="6" r="5" fill="var(--accent)"/><path d="M1 6h10M6 1c-2.5 3-2.5 7 0 10M6 1c2.5 3 2.5 7 0 10" stroke="#20252b" stroke-width="0.8" fill="none"/></svg>
        <span>www.lanternfieldadvisory.com</span>
      </div>
    </div>
  </section>

  <section class="card card-front" aria-label="Business card front">
    <div class="brand">
      <span class="brand-mark"></span>
      <span class="brand-name">Lanternfield Advisory</span>
    </div>
  </section>
</body>
</html>
```